National online rug retailer needs a home page design

See the MatsNowly logo and create a home page design around that color theme. Details are spelled out in word document uploaded below.

Apparently this website did not take my attachement showing the logo and basic requirements.  If you would send me your email address, I will send you the attachment directly.
Best regards,
Ned Ferris
nferris@qorvex.com

Target Market(s)

The target market is home owners 25 to 75 years old with combined incomes over $100,000 per year.

Industry/Entity Type

Online

Requirements
Must have
• Lots of white space with black letters and creative use of red and possibly one other color. Would like a compelling call to action button.

```html
<!DOCTYPE html>
<html lang="en">
<head>
<meta charset="utf-8">
<title>MatsNowly — Home</title>
<link href="https://fonts.googleapis.com/css2?family=Arimo:wght@400;700&family=Great+Vibes&display=swap" rel="stylesheet">
<style>
:root{
  --red:#d0161c;
  --red-dark:#a80f14;
  --ink:#1a1a1a;
  --text:#333;
  --muted:#777;
  --rule:#c9c9c9;
  --paper:#fff;
  --backdrop:#9c9c9c;
  --rug-deep:#6e2a22;
  --rug-mid:#a0553f;
  --rug-cream:#e9d3a8;
  --rug-tan:#c79a62;
}
*{box-sizing:border-box;margin:0;padding:0}
html,body{width:904px;height:1200px;overflow:hidden}
body{background:var(--backdrop);font-family:"Arimo",Arial,sans-serif;color:var(--text)}
.stage{position:absolute;left:0;top:0;width:1000px;height:1328px;transform:scale(.904);transform-origin:0 0;background:linear-gradient(135deg,#a3a3a3,#8f8f8f)}
.page{position:absolute;left:100px;top:0;width:800px;height:1300px;background:var(--paper)}
.abs{position:absolute}
a{color:inherit;text-decoration:none}
.topbar{left:0;top:0;width:800px;height:28px;background:#000;color:#fff;font-size:11px}
.account{position:absolute;right:150px;top:7px}
.account span{margin:0 6px;color:#aaa}
.cart{left:667px;top:0;width:110px;height:100px}
.cart-label{position:absolute;left:0;width:110px;top:48px;text-align:center;color:#fff;font-size:13px}
.brand{left:23px;top:54px;width:190px}
.brand-name{font-size:24px;line-height:28px;color:var(--red);font-weight:400;letter-spacing:-.3px;display:flex;align-items:center;gap:6px}
.brand-mark{width:12px;height:12px;background:var(--red);flex:none}
.brand-tag{font-size:8px;color:var(--muted);margin-top:6px;text-align:right}
.phone{left:391px;top:38px;font-size:12px;color:var(--ink)}
.phone a{color:var(--red)}
.search{left:233px;top:70px;width:400px;height:30px;border:1px solid #aaa;border-radius:15px;padding:0 15px;font-size:12px;color:#666;line-height:28px}
.search svg{position:absolute;right:10px;top:5px}
.nav{left:23px;top:122px;width:754px;height:32px;border-top:1px solid var(--rule);border-bottom:1px solid var(--rule);display:flex;align-items:center;font-size:9.5px;color:#444}
.nav a{flex:auto;text-align:center;border-left:1px solid var(--rule);line-height:16px}
.nav a:first-child{border-left:0;flex:0 0 72px}
.sidebar{left:23px;top:175px;width:140px;font-size:11px}
.side-title{font-size:11px;color:var(--ink);margin-bottom:16px}
.facet{border-bottom:1px solid var(--rule);padding:10px 0 14px}
.facet-head{display:flex;justify-content:space-between;font-size:10.5px;color:var(--ink);text-transform:uppercase}
.plus{width:9px;height:9px;border:1px solid #999;position:relative}
.plus::before,.plus::after{content:"";position:absolute;background:#999}
.plus::before{left:1px;right:1px;top:3px;height:1px}
.plus::after{top:1px;bottom:1px;left:3px;width:1px}
.facet ul{list-style:none;margin-top:10px}
.facet li{display:flex;justify-content:space-between;font-size:10.5px;line-height:18px}
.facet li b{color:var(--red);font-weight:400}
.slider{margin:18px 5px 0;height:4px;background:#ddd;border-radius:2px;position:relative}
.slider::before,.slider::after{content:"";position:absolute;top:-3px;width:10px;height:10px;border-radius:50%;background:#ddd;border:1px solid #ccc}
.slider::before{left:-5px}.slider::after{right:-5px}
.price-row{display:flex;justify-content:space-between;align-items:center;margin-top:14px;font-size:9.5px}
.cta{background:var(--red);color:#fff;font-size:9px;padding:4px 6px;border-radius:4px;border:1px solid var(--red-dark);box-shadow:0 0 0 1px #f3b0b0}
.banner{left:183px;top:177px;width:433px;height:176px;overflow:hidden;background:linear-gradient(180deg,#7b2a1e 0%,#a6422d 45%,#d9cdb7 62%,#e6dccb 100%)}
.banner-card{position:absolute;right:-5px;top:10px;width:160px;height:140px;background:linear-gradient(135deg,#2f7fd1,#174a9a);transform:rotate(12deg);border-radius:8px}
.banner-script{position:absolute;left:38px;top:30px;font-family:"Great Vibes",cursive;font-size:40px;color:#fff}
.banner-sub{position:absolute;left:38px;top:82px;font-size:27px;color:#fff;letter-spacing:.5px}
.banner-sub em{font-family:"Great Vibes",cursive;font-style:normal;font-size:32px}
.badge-off{position:absolute;left:329px;top:8px;width:98px;height:98px;border-radius:50%;background:var(--red);color:#fff;text-align:center;font-size:38px;line-height:36px;padding-top:16px}
.badge-off small{font-size:28px;display:block}
.section-title{font-size:13px;color:var(--ink);width:433px;border-bottom:1px solid var(--rule);padding-bottom:8px;font-weight:400}
.grid{display:grid;grid-template-columns:repeat(3,134px);column-gap:16px;row-gap:10px}
.product{width:134px;text-align:center;font-size:10.5px;position:relative}
.rug{width:134px;height:90px;border:3px solid #2a1612;background:radial-gradient(ellipse at center,var(--rug-cream) 0 8%,var(--rug-mid) 20%,var(--rug-deep) 60%,#3b1a14 100%)}
.product p{margin-top:8px;color:var(--text)}
.product .price,.suggest .price{color:var(--red);margin-top:2px}
.sale{position:absolute;left:84px;top:10px;width:37px;height:37px;border-radius:50%;background:var(--red);color:#fff;font-size:12px;line-height:37px}
.aside{left:635px;top:175px;width:141px}
.aside .section-title{width:141px;border:0;font-size:11px}
.suggest{text-align:center;font-size:10.5px;border-bottom:1px solid var(--rule);padding-bottom:16px;margin-bottom:16px}
.suggest .rug{width:141px;height:141px;border:1px solid #b7864f;background:radial-gradient(ellipse at center,#f2e4c3 0 40%,var(--rug-cream) 60%,var(--rug-tan) 100%)}
.footer{left:23px;top:1012px;width:754px;border-top:1px solid var(--rule)}
.fcol{position:absolute;top:20px;font-size:10.5px;line-height:16.4px}
.fcol h4{font-weight:400;font-size:11.5px;color:var(--ink);margin-bottom:9px}
.fcol ul{list-style:none;color:#444}
.seal{position:absolute;border-radius:5px}
.pay{position:absolute;top:142px;width:40px;height:25px;border-radius:2px}
.copyright{left:23px;top:1247px;width:754px;border-top:1px solid var(--rule);padding-top:14px;font-size:9.5px;color:var(--ink)}
</style>
</head>
<body>
<div class="stage">
<div class="page">

  <div class="abs topbar"><div class="account"><a>Sign in</a><span>|</span><a>Register</a></div></div>

  <div class="abs cart">
    <svg width="110" height="100" viewBox="0 0 110 100"><polygon points="0,0 110,0 110,96 55,86 0,96" fill="#d0161c"/>
      <g fill="none" stroke="#fff" stroke-width="1.6"><path d="M43 18h5l4 14h14l3-10H50"/><circle cx="54" cy="36" r="1.5"/><circle cx="64" cy="36" r="1.5"/></g>
    </svg>
    <div class="cart-label">0 items</div>
  </div>

  <div class="abs brand">
    <div class="brand-name"><span class="brand-mark"></span>MatsNowly.com</div>
    <div class="brand-tag">woven comfort, delivered home</div>
  </div>

  <div class="abs phone">Order toll-free: 1-800-555-0147 or <a>live chat online</a></div>

  <div class="abs search">enter keyword or item
    <svg width="20" height="18" viewBox="0 0 20 18"><circle cx="7" cy="7" r="5.5" fill="none" stroke="#444" stroke-width="2"/><path d="M11 11l6 5" stroke="#444" stroke-width="3"/></svg>
  </div>

  <nav class="abs nav"><a>HOME</a><a>SELECTION GUIDES</a><a>RUG CARE</a><a>FAQ</a><a>RETURN POLICY</a><a>FREE SHIPPING</a><a>CLEARANCE RUGS</a></nav>

  <aside class="abs sidebar">
    <div class="side-title">BROWSE BY</div>
    <div class="facet" style="padding-top:0"><div class="facet-head">Rug Theme<span class="plus"></span></div>
      <ul><li>Traditional<b>13</b></li><li>Transitional<b>12</b></li><li>Casual<b>11</b></li></ul></div>
    <div class="facet" style="padding-top:16px"><div class="facet-head">Color Way<span class="plus"></span></div>
      <ul><li>Black<b>13</b></li><li>Blue<b>12</b></li><li>Green<b>11</b></li><li>Gold<b>10</b></li></ul></div>
    <div class="facet" style="padding:18px 0 18px"><div class="facet-head">Price</div>
      <div class="slider"></div>
      <div class="price-row"><span>Price: $0 - $1234</span><a class="cta">FILTER</a></div></div>
    <div class="facet" style="padding:18px 0 16px"><div class="facet-head">Size<span class="plus"></span></div></div>
    <div class="facet" style="padding:16px 0 16px"><div class="facet-head">Shape<span class="plus"></span></div></div>
    <div class="facet" style="padding:16px 0 16px"><div class="facet-head">Fiber Content<span class="plus"></span></div></div>
    <div class="facet" style="padding:16px 0 16px"><div class="facet-head">Mfgr. Brand<span class="plus"></span></div></div>
    <div class="facet" style="padding:16px 0 16px"><div class="facet-head">Mfgr. Collection<span class="plus"></span></div></div>
  </aside>

  <div class="abs banner" role="img" aria-label="Close-up of a red and cream shag rug with a payment card">
    <div class="banner-card"></div>
    <div class="banner-script">Summer Sale</div>
    <div class="banner-sub">GET DISCOUNT <em>with</em></div>
    <div class="badge-off">30%<small>Off</small></div>
  </div>

  <section class="abs" style="left:183px;top:366px">
    <h3 class="section-title">NEW ARRIVALS</h3>
    <div class="grid" style="margin-top:16px">
      <div class="product"><div class="rug" role="img" aria-label="Red Persian medallion rug"></div><span class="sale">SALE</span><p>Elegant Rug</p><p class="price">$150</p></div>
      <div class="product"><div class="rug" role="img" aria-label="Red Persian medallion rug"></div><p>Elegant Rug</p><p class="price">$150</p></div>
      <div class="product"><div class="rug" role="img" aria-label="Red Persian medallion rug"></div><p>Elegant Rug</p><p class="price">$150</p></div>
      <div class="product"><div class="rug" role="img" aria-label="Red Persian medallion rug"></div><p>Elegant Rug</p><p class="price">$150</p></div>
      <div class="product"><div class="rug" role="img" aria-label="Red Persian medallion rug"></div><span class="sale">SALE</span><p>Elegant Rug</p><p class="price">$150</p></div>
      <div class="product"><div class="rug" role="img" aria-label="Red Persian medallion rug"></div><p>Elegant Rug</p><p class="price">$150</p></div>
    </div>
  </section>

  <section class="abs" style="left:183px;top:683px">
    <h3 class="section-title">BEST OF THE MONTH</h3>
    <div class="grid" style="margin-top:16px">
      <div class="product"><div class="rug" role="img" aria-label="Red Persian medallion rug"></div><span class="sale">SALE</span><p>Elegant Rug</p><p class="price">$150</p></div>
      <div class="product"><div class="rug" role="img" aria-label="Red Persian medallion rug"></div><p>Elegant Rug</p><p class="price">$150</p></div>
      <div class="product"><div class="rug" role="img" aria-label="Red Persian medallion rug"></div><p>Elegant Rug</p><p class="price">$150</p></div>
      <div class="product"><div class="rug" role="img" aria-label="Red Persian medallion rug"></div><p>Elegant Rug</p><p class="price">$150</p></div>
      <div class="product"><div class="rug" role="img" aria-label="Red Persian medallion rug"></div><span class="sale">SALE</span><p>Elegant Rug</p><p class="price">$150</p></div>
      <div class="product"><div class="rug" role="img" aria-label="Red Persian medallion rug"></div><p>Elegant Rug</p><p class="price">$150</p></div>
    </div>
  </section>

  <aside class="abs aside">
    <h3 class="section-title" style="margin-bottom:10px">YOU MAY ALSO LIKE</h3>
    <div class="suggest"><div class="rug" role="img" aria-label="Cream classic floral rug"></div><p style="margin-top:6px">Classic Rug</p><p class="price">$200</p></div>
    <div class="suggest"><div class="rug" role="img" aria-label="Cream classic floral rug"></div><p style="margin-top:6px">Classic Rug</p><p class="price">$200</p></div>
    <div class="suggest"><div class="rug" role="img" aria-label="Cream classic floral rug"></div><p style="margin-top:6px">Classic Rug</p><p class="price">$200</p></div>
  </aside>

  <footer class="abs footer">
    <div class="fcol" style="left:1px"><h4>Customer Service</h4><ul><li>Shipping</li><li>Return Policy</li><li>Privacy Policy</li><li>Ordering &amp; Delivery Checklist</li><li>Terms of Use</li><li>Terms of Sale</li><li>Contact Us</li><li>Environmental Policy</li></ul></div>
    <div class="fcol" style="left:181px"><h4>Resources</h4><ul><li>Product Articles</li><li>Learning Center</li><li>Help</li><li>Refer A Friend</li><li>MatsNowly Blog</li><li>Room Scene Viewer</li><li>Site Map</li><li>FAQ</li><li>Customer Testimonials</li><li>Photo Gallery</li></ul></div>
    <div class="fcol" style="left:345px"><h4>Corporate Info</h4><ul><li>About MatsNowly.com</li><li>Careers</li><li>Affiliates</li></ul></div>
    <div class="fcol" style="left:525px;width:230px;height:200px"><h4>Power by</h4>
      <div class="seal" style="left:0;top:28px;width:96px;height:36px;background:#174e7a"></div>
      <div class="seal" style="left:111px;top:28px;width:102px;height:38px;background:#eef2f6;border:1px solid #9aa"></div>
      <div class="seal" style="left:0;top:76px;width:96px;height:36px;background:#f2f2f2;border:1px solid #ccc;border-radius:18px"></div>
      <div class="pay" style="left:0;background:#2c7cc1"></div>
      <div class="pay" style="left:47px;background:#f3f3f3;border:1px solid #ccc"></div>
      <div class="pay" style="left:94px;background:#fbe3a0;border:1px solid #e0c070"></div>
      <div class="pay" style="left:141px;background:#1f2d5a"></div>
      <div class="pay" style="left:188px;background:#f3f3f3;border:1px solid #ccc"></div>
    </div>
  </footer>

  <div class="abs copyright">Copyright (c) 2013 MatsNowly. Allrights reserved.</div>
</div>
</div>
</body>
</html>
```